Logo and website for new private wealth management business

This project is for a new company website and logo. The name of the firm is Harborline Estate Partners, LLC. We are a wealth management firm offering customized financial planning and investment management services to high net worth and ultra high net worth individuals and families. I want the website to feel contemporary but convey a feeling of sophistication and prestige.
www.tolvanridgeholdings.example and www.qnfunds.example are both good reference websites.
My clients will consist of wealthy individuals and families. I have existing clients in their 50s - 70s, but I also intend to target younger business owners and entrepreneurs in their 30s -50s.

Target Market(s)

Business owners, entrepreneurs and corporate executives. Many existing clients are in their 60s and 70s, but intend to also attract a younger clientele in their 30s - 50s.

Industry/Entity Type

Wealth management, investment advisory, financial planning

Coding

Coded - Design and coding required

Colors
0054AA
0677BA
7BADD7
CADEEF
E8F1F8
0094D4
00A9DD
6FCCEA
C7EBF8
E9F6FB
00AB8E
00BBA5
67D7C9
C6EFE9
E9F9F6
EE7325
F08F49
F5BC92
FAE3D3
FDF4ED

Requirements
Must have
• Should use blue as the main color theme. Should have an About, Services, Our Clients, FAQ, and Contact sections
Should not have
• Should not have pictures of people as the background.

```html
<!DOCTYPE html>
<html lang="en">
<head>
<meta charset="utf-8">
<title>Harborline Estate Partners, LLC</title>
<link href="https://fonts.googleapis.com/css2?family=Lora:wght@400;500;600&family=Mulish:wght@400;600;700&display=swap" rel="stylesheet">
<style>
:root{
  --blue:#0054AA;--blue-mid:#0677BA;--blue-soft:#E8F1F8;--sky:#7BADD7;
  --green:#00AB8E;--green-2:#00BBA5;--mint:#C6EFE9;--mint-2:#E9F9F6;
  --ink:#1d2a3a;--text:#3b4656;--white:#fff;
}
*{box-sizing:border-box;margin:0;padding:0}
html,body{width:1200px;height:3382px;overflow:hidden;background:#fff}
body{position:relative;font-family:'Mulish',sans-serif;color:var(--text)}
.abs{position:absolute}
.serif{font-family:'Lora',serif}
.btn{position:absolute;background:var(--green);color:#fff;font-family:'Lora',serif;font-weight:600;display:flex;align-items:center;justify-content:center;border-radius:3px;white-space:nowrap}
.label{position:absolute;font-size:11px;font-weight:700;letter-spacing:.2px;color:var(--ink);text-transform:uppercase;white-space:nowrap}
.label::before{content:"";position:absolute;left:-71px;top:6px;width:53px;height:2px;background:var(--green)}
.h2{position:absolute;font-family:'Lora',serif;color:var(--ink);font-size:34px;line-height:39px;white-space:nowrap}

/* header */
.brand{left:110px;top:20px;width:240px;text-align:center}
.brand .mark{width:40px;height:40px;border-radius:50%;background:var(--green);margin:0 auto 10px}
.brand .name{font-family:'Lora',serif;font-size:14px;color:var(--blue);padding-top:6px;border-top:2px solid var(--green);white-space:nowrap;margin:0 10px}
.follow{left:633px;top:34px;font-family:'Lora',serif;font-size:15px;color:#444}
.soc{width:32px;height:32px;border-radius:50%;top:27px}
.advisor{left:940px;top:23px;font-family:'Lora',serif;font-size:15px;color:#444;line-height:22px;white-space:nowrap}
.advisor b{font-weight:400;color:var(--blue);font-size:17px}
.vrule{left:920px;top:16px;width:1px;height:50px;background:var(--sky)}
.nav{top:86px;font-family:'Lora',serif;font-size:15px;color:#222;white-space:nowrap}
.nav.active{color:var(--green);font-weight:600}

/* hero */
.hero{left:0;top:122px;width:1200px;height:555px;background:linear-gradient(120deg,#6f7f32 0%,#a7a447 35%,#d9b65a 60%,#8e9a3c 100%)}
.hero-box{left:125px;top:272px;width:361px;height:214px;background:rgba(0,84,170,.72);padding:18px 0 0 27px}
.hero-box h1{font-family:'Lora',serif;font-weight:400;color:#fff;font-size:32px;line-height:37px;white-space:nowrap}
.dot{top:629px;width:12px;height:12px;border-radius:50%;border:2px solid #fff}
.dot.on{background:var(--green)}

/* services */
.svc{position:absolute;top:850px;width:200px}
.svc .ic{position:absolute;left:3px;top:0;width:58px;height:58px;border-radius:50%;background:var(--mint)}
.svc h3{position:absolute;left:75px;top:10px;font-family:'Lora',serif;font-weight:400;font-size:17px;line-height:20px;color:var(--ink);white-space:nowrap}
.svc .rule{position:absolute;left:2px;top:76px;width:177px;height:2px;background:var(--blue)}
.svc p{position:absolute;left:3px;top:100px;width:185px;font-size:12px;line-height:16px}
.svc .btn{top:239px;left:5px;width:75px;height:29px;font-size:11px}

/* about */
.band{left:0;width:1200px;background:var(--blue-soft)}
.card{position:absolute;background:#fff;border-radius:2px}
.card .ic{width:56px;height:56px;border-radius:50%;background:var(--mint);position:absolute}
.card h4{position:absolute;font-family:'Lora',serif;font-weight:400;font-size:17px;color:var(--ink);width:100%;text-align:center}
.card p{position:absolute;font-size:11px;line-height:14.5px;text-align:center}
.about-p{left:656px;top:1460px;width:384px;font-size:13px;line-height:18.4px}

/* closer look */
.photo{position:absolute}
.bullets{left:142px;top:2058px;width:360px;list-style:none}
.bullets li{position:absolute;left:0;padding-left:19px;font-size:13px;line-height:19px;width:360px}
.bullets li::before{content:"";position:absolute;left:0;top:8px;width:8px;height:8px;border-radius:50%;background:var(--blue)}

/* resources */
.res{position:absolute;top:2560px;width:252px;height:258px;background:#fff;padding:26px 26px}
.res h5{font-family:'Lora',serif;font-weight:400;font-size:16px;line-height:20px;color:var(--ink)}
.res p{margin-top:18px;font-size:12px;line-height:17px}
.res .btn{left:27px;top:207px;width:75px;height:27px;font-size:11px}

/* cta + footer */
.cta{left:0;top:2886px;width:1200px;height:167px;background:var(--blue)}
.cta p{position:absolute;left:131px;top:54px;font-family:'Lora',serif;color:#fff;font-size:25px;line-height:36px;white-space:nowrap}
.footer{left:0;top:3053px;width:1200px;height:329px;background:var(--green);color:#fff}
.fh{position:absolute;top:36px;font-size:13px;font-weight:700;letter-spacing:.5px}
.fi{position:absolute;font-size:12px;line-height:16px;white-space:nowrap}
.fic{position:absolute;width:24px;height:24px;border-radius:50%;background:#fff}
.menu{position:absolute;left:790px;top:74px;font-size:12px;line-height:24px;list-style:none}
</style>
</head>
<body>

<!-- header -->
<div class="abs brand"><div class="mark"></div><div class="name">Harborline Estate Partners, LLC</div></div>
<div class="abs follow">Follow us</div>
<div class="abs soc" style="left:714px;background:#3b5998"></div>
<div class="abs soc" style="left:762px;background:#38a1f3"></div>
<div class="abs soc" style="left:810px;background:#e1306c"></div>
<svg class="abs" style="left:870px;top:28px" width="30" height="30" viewBox="0 0 24 24" fill="none" stroke="#0054AA" stroke-width="1.6"><path d="M5 3h4l2 5-2.5 1.5a11 11 0 0 0 6 6L16 13l5 2v4a2 2 0 0 1-2 2A17 17 0 0 1 3 5a2 2 0 0 1 2-2z"/><path d="M15 3a6 6 0 0 1 6 6M15 6.5a2.5 2.5 0 0 1 2.5 2.5"/></svg>
<div class="abs vrule"></div>
<div class="abs advisor">Talk to an advisor<br><b>+1 555 014 2760</b></div>
<div class="abs nav active" style="left:489px">Home</div>
<div class="abs nav" style="left:567px">How We Help</div>
<div class="abs nav" style="left:700px">About Us</div>
<div class="abs nav" style="left:802px">Solutions</div>
<div class="abs nav" style="left:907px">Services</div>
<div class="abs nav" style="left:993px">Contact Us</div>

<!-- hero -->
<div class="abs hero" role="img" aria-label="Sunlit outdoor photo of a family walking through a park"></div>
<div class="abs hero-box"><h1>Wealth management<br>for individuals and<br>families</h1></div>
<div class="btn" style="left:152px;top:419px;width:113px;height:37px;font-size:14px">Read More</div>
<div class="abs dot" style="left:144px"></div>
<div class="abs dot on" style="left:162px"></div>
<div class="abs dot" style="left:179px"></div>
<div class="abs dot" style="left:196px"></div>

<!-- services -->
<div class="label" style="left:202px;top:738px">Areas of Practice</div>
<div class="h2" style="left:130px;top:762px">Our Services</div>

<div class="svc" style="left:131px"><div class="ic"></div>
<svg class="abs" style="left:17px;top:14px" width="30" height="30" viewBox="0 0 24 24" fill="none" stroke="#0054AA" stroke-width="1.4"><rect x="4" y="3" width="14" height="18" rx="1"/><path d="M7 7h8M7 11h3M12 11h3M7 15h3M12 15h3"/></svg>
<h3>Financial<br>Planning</h3><div class="rule"></div>
<p>There are many variations of passages of Lorem Ipsum avai lable, but the majority have suffered alteration in some form, by injected humour, or rand omised words which don't look even slightly believable</p>
<div class="btn">Read More</div></div>

<div class="svc" style="left:366px"><div class="ic"></div>
<svg class="abs" style="left:17px;top:14px" width="30" height="30" viewBox="0 0 24 24" fill="none" stroke="#0054AA" stroke-width="1.4"><path d="M6 4h12l4 5-10 12L2 9z"/><path d="M2 9h20M9 4l3 17 3-17"/></svg>
<h3>Wealth<br>Management</h3><div class="rule"></div>
<p>There are many variations of passages of Lorem Ipsum avai lable, but the majority have suffered alteration in some form, by injected humour, or rand omised words which don't look even slightly believable</p>
<div class="btn">Read More</div></div>

<div class="svc" style="left:628px"><div class="ic"></div>
<svg class="abs" style="left:17px;top:14px" width="30" height="30" viewBox="0 0 24 24" fill="none" stroke="#0054AA" stroke-width="1.4"><circle cx="13" cy="8" r="4"/><path d="M2 16l5-2h5l-4 3M2 20l6-1 10-5"/></svg>
<h3>Investment<br>Management</h3><div class="rule"></div>
<p>There are many variations of passages of Lorem Ipsum avai lable, but the majority have suffered alteration in some form, by injected humour, or rand omised words which don't look even slightly believable</p>
<div class="btn">Read More</div></div>

<div class="svc" style="left:889px"><div class="ic"></div>
<svg class="abs" style="left:17px;top:14px" width="30" height="30" viewBox="0 0 24 24" fill="none" stroke="#0054AA" stroke-width="1.4"><path d="M4 14v-3a8 8 0 0 1 16 0v3"/><rect x="3" y="13" width="4" height="6" rx="1"/><rect x="17" y="13" width="4" height="6" rx="1"/></svg>
<h3>Support<br>What matters</h3><div class="rule"></div>
<p>There are many variations of passages of Lorem Ipsum avai lable, but the majority have suffered alteration in some form, by injected humour, or rand omised words which don't look even slightly believable</p>
<div class="btn">Read More</div></div>

<!-- about -->
<div class="abs band" style="top:1200px;height:593px"></div>
<div class="card" style="left:131px;top:1253px;width:218px;height:257px">
  <div class="ic" style="left:81px;top:27px"></div>
  <svg class="abs" style="left:96px;top:42px" width="26" height="26" viewBox="0 0 24 24" fill="none" stroke="#0054AA" stroke-width="1.4"><rect x="3" y="5" width="18" height="15" rx="1"/><path d="M3 9h18M8 3v4M16 3v4M8 14l3 3 5-5"/></svg>
  <h4 style="top:106px">Tailored</h4>
  <p style="left:20px;top:142px;width:178px">There are many variations of passages of Lorem Ipsum avai lable, but the majority have suffered alteration in some form, by injected humour, or rand omised words which.</p>
</div>
<div class="card" style="left:369px;top:1291px;width:218px;height:257px">
  <div class="ic" style="left:81px;top:27px"></div>
  <svg class="abs" style="left:96px;top:42px" width="26" height="26" viewBox="0 0 24 24" fill="none" stroke="#0054AA" stroke-width="1.4"><path d="M3 21h18M5 21v-6M9 21v-9M13 21v-5"/><circle cx="17" cy="8" r="4"/></svg>
  <h4 style="top:108px">Stable</h4>
  <p style="left:20px;top:146px;width:178px">There are many variations of passages of Lorem Ipsum avai lable, but the majority have suffered alteration in some form, by injected humour, or rand omised words which.</p>
</div>
<div class="card" style="left:133px;top:1576px;width:455px;height:154px">
  <div class="ic" style="left:40px;top:49px"></div>
  <svg class="abs" style="left:55px;top:64px" width="26" height="26" viewBox="0 0 24 24" fill="none" stroke="#0054AA" stroke-width="1.4"><path d="M9 17h6M10 20h4M8 14a6 6 0 1 1 8 0c-1 1-1 2-1 3H9c0-1 0-2-1-3z"/></svg>
  <h4 style="left:129px;top:33px;width:auto;text-align:left">Resourceful</h4>
  <p style="left:129px;top:64px;width:260px;text-align:left">There are many variations of passages of Lorem Ipsum avai lable, but the majority have suffered alteration in some form, by injected humour, or rand omised words which.</p>
</div>
<div class="label" style="left:728px;top:1317px">About Us</div>
<div class="h2" style="left:655px;top:1352px">A values-based approach<br>to your wealth</div>
<p class="abs about-p">Sed ut perspiciatis unde omnis iste natus error sit voluptatem accusantium doloremque laudantium, totam rem aperiam, eaque ipsa quae ab illo inventore veritatis et quasi architecto beatae vitae dicta sunt explicabo. Nemo enim ipsam voluptatem quia voluptas sit aspernatur aut odit aut fugit, sed quia consequuntur magni dolores eos qui ratione voluptatem sequi nesciunt. Neque porro quisquam est, qui dolorem ipsum quia dolor sit amet, consectetur, adipisci velit, sed quia non numquam eius modi tempora incidunt ut labore et dolore magnam aliquam</p>
<div class="btn" style="left:659px;top:1653px;width:89px;height:32px;font-size:13px">Read More</div>

<!-- closer look -->
<div class="label" style="left:204px;top:1864px">Take a Closer Look</div>
<div class="h2" style="left:131px;top:1898px;font-size:35px;line-height:38.5px">Lorem ipsum dolor sit<br>amet consectetur<br>adipiscing eli</div>
<ul class="abs bullets">
  <li style="top:0">Sed ut perspiciatis unde omnis iste natus error sit volupt atem accusantium doloremque laudantium.</li>
  <li style="top:62px">Aenean quis mauris a nunc facilisis vehicula posuere condimentum nibh.</li>
  <li style="top:121px">Praesent maximus risus eu dolor pellentesque, eu consequat elit accumsan.</li>
  <li style="top:184px">Fusce pharetra lectus sed leo rutrum, vitae facilisis nisl tempus.</li>
  <li style="top:249px">Nam id quam aliquet, imperdiet lorem eget, elementum augue.</li>
</ul>
<div class="photo" style="left:587px;top:1793px;width:613px;height:599px;background:linear-gradient(135deg,#5b6b73 0%,#7a5546 45%,#3c2a24 100%)" role="img" aria-label="Photo of an advisor and client talking on a sofa in an office lounge"></div>

<!-- resources -->
<div class="abs band" style="top:2392px;height:494px"></div>
<div class="label" style="left:203px;top:2453px">Take a Closer Look</div>
<div class="h2" style="left:130px;top:2476px">Resources</div>
<svg class="abs" style="left:998px;top:2464px" width="20" height="30" viewBox="0 0 20 30" fill="none" stroke="#0054AA" stroke-width="2.4"><path d="M15 3 4 15l11 12"/></svg>
<svg class="abs" style="left:1043px;top:2464px" width="20" height="30" viewBox="0 0 20 30" fill="none" stroke="#0054AA" stroke-width="2.4"><path d="M5 3l11 12L5 27"/></svg>

<div class="res" style="left:131px"><h5>Lorem ipsum dolor sit ametconsectetur adipis cing eli</h5><p>Sed ut perspiciatis unde omnis iste natus error sit voluptatem accusantium doloremque laudantium, totam rem aperiam, eaque ipsa quae ab</p><div class="btn">Read More</div></div>
<div class="res" style="left:407px"><h5>Lorem ipsum dolor sit ametconsectetur adipis cing eli</h5><p>Sed ut perspiciatis unde omnis iste natus error sit voluptatem accusantium doloremque laudantium, totam rem aperiam, eaque ipsa quae ab</p><div class="btn">Read More</div></div>
<div class="res" style="left:680px"><h5>Lorem ipsum dolor sit ametconsectetur adipis cing eli</h5><p>Sed ut perspiciatis unde omnis iste natus error sit voluptatem accusantium doloremque laudantium, totam rem aperiam, eaque ipsa quae ab</p><div class="btn">Read More</div></div>
<div class="res" style="left:954px"><h5>Lorem ipsum dolor sit ametconsectetur adipis cing eli</h5><p>Sed ut perspiciatis unde omnis iste natus error sit voluptatem accusantium doloremque laudantium, totam rem aperiam, eaque ipsa quae ab</p><div class="btn">Read More</div></div>

<!-- cta -->
<div class="abs cta">
  <p>Nam id quam aliquet imperdiet lorem<br>eget elementum augue.</p>
  <div class="btn" style="left:930px;top:51px;width:137px;height:49px;font-size:18px;border-radius:4px">Contact Us</div>
</div>

<!-- footer -->
<footer class="abs footer">
  <div class="abs" style="left:233px;top:95px;width:40px;height:40px;border-radius:50%;background:#fff"></div>
  <div class="abs" style="left:150px;top:138px;width:202px;height:2px;background:#fff"></div>
  <div class="abs serif" style="left:120px;top:147px;width:262px;text-align:center;font-size:15px;white-space:nowrap">Harborline Estate Partners, LLC</div>

  <div class="fh" style="left:435px">CONTACT US</div>
  <div class="fic" style="left:435px;top:78px"></div>
  <div class="fi" style="left:467px;top:76px">Suite 204, Level 2 West,<br>41-47 Marlow Quay, Easton Bay 4410.</div>
  <div class="fic" style="left:435px;top:134px"></div>
  <div class="fi" style="left:467px;top:132px">Call Us<br>+1 555 014 2760</div>
  <div class="fic" style="left:435px;top:187px"></div>
  <div class="fi" style="left:467px;top:185px">E mail Us<br>info@harborlineestate.example</div>

  <div class="fh" style="left:790px">MENU</div>
  <ul class="menu"><li>HOME</li><li>HOW WE HELP</li><li>ABOUT US</li><li>SOLUTIONS</li><li>SERVICES</li><li>CONTACT US</li></ul>

  <div class="fh" style="left:966px">FOLLOW US</div>
  <div class="fic" style="left:966px;top:84px"></div>
  <div class="fi" style="left:1000px;top:76px">Like us on<br>PAGEHUB</div>
  <div class="fic" style="left:966px;top:134px"></div>
  <div class="fi" style="left:1000px;top:126px">Follow us on<br>CHIRPLINE</div>
  <div class="fic" style="left:966px;top:186px"></div>
  <div class="fi" style="left:1000px;top:178px">Follow us on<br>WORKNET</div>

  <div class="abs" style="left:131px;top:250px;width:938px;height:1px;background:rgba(255,255,255,.35)"></div>
  <div class="abs" style="left:0;top:283px;width:1200px;text-align:center;font-size:11px">Copyright © 2022 All Rights Reserved</div>
</footer>

</body>
</html>
```